Business card and company logo design needed

Need a business card and company logo design for all stationary for an Aviation refueling consultancy business. Our business offers consulting services in the specialist aviation refueling industry. Services range from engineering, compliance and management consultancy through to project management services. This encompasses infrastructure from refinery through to airport and into the aircraft wing.

Design should be simple, 'less-is-more' concept, possibly taking advantage of the 'm' for tovel and the fact is it the aviation industry. It should convey confidence, safety, experience, professionalism, aviation, engineering?, and should not be afraid to be simple in color...though please do not let this restrict your designs and imagination.

Target Market(s)

Airport authorities, oil majors, aircraft operators

Industry/Entity Type

Airport

Contact Information for Business Card

Verlin Skyward Advisory Pty Ltd
Dario Tovel
Director
mobile:+61428537104
email: dario@tovelexample.com
Skype: dario.tovelexample

Logo styles of interest
Emblem Logo
Pictorial/Combination Logo
Abstract Logo
Wordmark Logo
Lettermark Logo
Requirements
Must have
• - A feel of safety, security and confidence
Nice to have
• - Aviation has both heritage and modern 'sexy' elements so would be nice to try and capture both
- Aviation 'JET' fuel color is designated as black in signage or labels
- Themes? : Aviation fuel is derived from oil, it burns, safety, Jet fuel is colorless
- Company is global in reach, borderless like aircraft
Should not have
• - Cliche:

```html
<!DOCTYPE html>
<html lang="en">
<head>
<meta charset="utf-8">
<title>Verlin Skyward Advisory – Business Card</title>
<link rel="stylesheet" href="https://fonts.googleapis.com/css2?family=Questrial&display=swap">
<style>
  :root {
    --card-white: #ffffff;
    --fuel-black: #000000;
    --brand-green: #078a10;
    --ink: #111111;
    --font-main: "Questrial", "Century Gothic", sans-serif;
  }
  html, body {
    margin: 0;
    padding: 0;
    overflow: hidden;
    background: var(--card-white);
  }
  .card {
    position: relative;
    width: 1200px;
    height: 695px;
    overflow: hidden;
    background: var(--card-white);
    font-family: var(--font-main);
  }
  .card__sweep {
    position: absolute;
    inset: 0;
  }
  .contact-top {
    position: absolute;
    top: 50px;
    right: 42px;
    text-align: right;
    color: var(--brand-green);
    font-size: 35px;
    line-height: 42px;
    letter-spacing: 0.3px;
  }
  .holder {
    position: absolute;
    top: 322px;
    right: 50px;
    text-align: right;
    color: var(--ink);
  }
  .holder__name {
    font-size: 47px;
    line-height: 56px;
    margin: 0;
    font-weight: 400;
  }
  .holder__role {
    font-size: 38px;
    line-height: 46px;
    margin: 0 6px 0 0;
  }
  .contact-mobile {
    position: absolute;
    top: 606px;
    right: 44px;
    color: var(--brand-green);
    font-size: 35px;
    line-height: 42px;
  }
  .brand {
    position: absolute;
    left: 60px;
    top: 378px;
    color: var(--brand-green);
  }
  .brand__row {
    display: flex;
    align-items: center;
    gap: 26px;
    margin-left: 32px;
  }
  .brand__name {
    font-size: 74px;
    line-height: 80px;
    letter-spacing: 4px;
  }
  .brand__dot {
    width: 46px;
    height: 46px;
    border-radius: 50%;
    background: var(--brand-green);
  }
  .brand__company {
    font-size: 31px;
    line-height: 40px;
    margin-top: 18px;
    letter-spacing: 0.5px;
  }
</style>
</head>
<body>
  <div class="card">
    <svg class="card__sweep" width="1200" height="695" viewBox="0 0 1200 695" aria-hidden="true">
      <path d="M0,0 H185 C560,40 790,230 755,420 C735,540 680,630 620,695 H0 Z"
            fill="var(--fuel-black)" stroke="var(--brand-green)" stroke-width="10"/>
    </svg>

    <div class="contact-top">
      <div class="contact-top__email">Email: dario@tovelexample.com</div>
      <div class="contact-top__skype">Skype: dario.tovelexample</div>
    </div>

    <div class="holder">
      <h1 class="holder__name">Dario Tovel</h1>
      <p class="holder__role">Director</p>
    </div>

    <div class="contact-mobile">mobile:+61428537104</div>

    <div class="brand">
      <div class="brand__row">
        <span class="brand__name">TOVEL</span>
        <span class="brand__dot"></span>
      </div>
      <div class="brand__company">Verlin Skyward Advisory Pty Ltd</div>
    </div>
  </div>
</body>
</html>
```